Business Card Design

I am an Event and Wedding Planner in need of an eye catching business card featuring my logo (attached), my contact details, and my company tagline (Making each one of your gatherings radiant...) I would like the tagline in font similar the logo's font.
Updates
I have just noticed that my logo has a misspelling so for the final design, I will be uploading a corrected logo as soon as I have it.
My apologies.
Reason: Waiting on a corrected logo...Occasions is misspelled and it should say Weddings not Wedding
The logo has been corrected so now Occasions is spelled correctly and it says Weddings instead of Wedding. Please use Edwardian Script ITC as the font for the tagline so it will match the logo. Thank you for your patience.
Target Market(s)
Engaged couples and people hosting milestone celebrations. 25-50 years old, predominately female
Industry/Entity Type
Business
Contact Information for Business Card
Delphine Marsh, Event Manager / Owner, Mobile: 0491 836 254, Email: delphine@radiantgatheringsco.com.au, www.radiantgatheringsco.com.au, Making each one of your gatherings radiant...

```html
<!DOCTYPE html>
<html lang="en">
<head>
<meta charset="utf-8">
<title>Radiant Gatherings Co. — Business Card</title>
<link rel="stylesheet" href="https://fonts.googleapis.com/css2?family=EB+Garamond:wght@400&family=Pinyon+Script&display=swap">
<style>
  :root {
    --stage: #e9e6e3;
    --card-red: #ec2326;
    --card-white: #f7f6f4;
    --card-black: #050505;
    --salmon: #d98a78;
    --pattern-red: #e8504a;
    --ink-white: #ffffff;
    --ink-grey: #d9d9d9;
    --floral-rose: #e7a595;
    --floral-leaf: #7aa34a;
    --sketch-cream: #e9e1d2;
    --sketch-ink: #3a3a3a;
  }
  * { box-sizing: border-box; margin: 0; padding: 0; }
  html, body { width: 1200px; height: 900px; overflow: hidden; }
  body {
    background: var(--stage);
    position: relative;
    font-family: "EB Garamond", Georgia, serif;
  }
  .card {
    position: absolute;
    width: 600px;
    height: 365px;
    overflow: hidden;
    box-shadow: 0 10px 24px rgba(0,0,0,.22);
  }

  /* Back face */
  .card-back {
    left: 540px; top: 50px;
    background: var(--card-black);
    color: var(--ink-white);
  }
  .card-back .brand {
    position: absolute; left: 150px; top: 44px;
    width: 230px; text-align: center;
    font-size: 34px; line-height: 1.05;
    color: var(--ink-white);
  }
  .card-back .brand-rule {
    position: absolute; left: 175px; top: 126px;
    width: 180px; height: 1px; background: var(--ink-grey);
  }
  .card-back .tagline {
    position: absolute; left: 120px; top: 145px;
    width: 300px;
    font-family: "Pinyon Script", cursive;
    font-size: 24px; line-height: 1.3;
    color: var(--ink-grey);
  }
  .card-back .email {
    position: absolute; left: 26px; top: 300px;
    font-size: 14px; letter-spacing: .2px;
    color: var(--ink-white);
  }
  .card-back .floral {
    position: absolute; right: 30px; bottom: 28px;
    width: 250px; height: 130px;
    border-radius: 60px 60px 20px 60px;
    background: radial-gradient(ellipse at 60% 50%, var(--floral-rose) 0%, rgba(231,165,149,.6) 40%, rgba(122,163,74,.45) 65%, rgba(0,0,0,0) 80%);
  }
  .card-back .edge-band {
    position: absolute; left: 0; right: 0; bottom: 0;
    height: 12px; background: var(--salmon);
  }

  /* Front face */
  .card-front {
    left: 70px; top: 480px;
    background: var(--card-red);
    color: var(--ink-white);
  }
  .card-front .side-panel {
    position: absolute; left: 0; top: 0; bottom: 0;
    width: 222px; background: var(--card-white);
  }
  .card-front .side-panel .tagline {
    position: absolute; left: 22px; top: 22px; width: 190px;
    font-family: "Pinyon Script", cursive;
    font-size: 19px; line-height: 1.3;
    color: var(--card-red);
  }
  .card-front .side-panel .sketch {
    position: absolute; left: 28px; top: 120px;
    width: 110px; height: 210px;
    border-radius: 50px;
    background: linear-gradient(180deg, rgba(58,58,58,.12), var(--sketch-cream) 60%, rgba(58,58,58,.18));
  }
  .card-front .pattern-strip {
    position: absolute; left: 222px; top: 0; bottom: 0;
    width: 24px;
    background: linear-gradient(90deg, var(--pattern-red), #f08a84);
  }
  .card-front .details {
    position: absolute; left: 246px; right: 0; top: 0; bottom: 0;
    text-align: center;
  }
  .card-front .brand {
    margin-top: 40px;
    font-size: 30px; line-height: 1.05;
    color: var(--ink-white);
  }
  .card-front .brand-rule {
    width: 170px; height: 1px; margin: 12px auto 16px;
    background: var(--ink-white);
  }
  .card-front .name { font-size: 30px; line-height: 1.1; }
  .card-front .role { font-size: 15px; margin-top: 2px; }
  .card-front .contact {
    position: absolute; left: 0; right: 0; bottom: 40px;
    font-size: 15px; line-height: 1.5;
  }
</style>
</head>
<body>

  <section class="card card-back" aria-label="Business card, back">
    <div class="brand">Radiant<br>Gatherings Co.</div>
    <div class="brand-rule"></div>
    <p class="tagline">Making each one of your gatherings radiant...</p>
    <p class="email">delphine@radiantgatheringsco.com.au</p>
    <div class="floral" role="img" aria-label="Folk-style floral illustration in rose pink and leaf green"></div>
    <div class="edge-band"></div>
  </section>

  <section class="card card-front" aria-label="Business card, front">
    <div class="side-panel">
      <p class="tagline">Making each one of your gatherings radiant...</p>
      <div class="sketch" role="img" aria-label="Fine line drawing of climbing flowers and swirling stems"></div>
    </div>
    <div class="pattern-strip" role="img" aria-label="Vertical band of small red diamond pattern"></div>
    <div class="details">
      <div class="brand">Radiant<br>Gatherings Co.</div>
      <div class="brand-rule"></div>
      <p class="name">Delphine Marsh</p>
      <p class="role">Event Manager</p>
      <p class="contact">www.radiantgatheringsco.com.au<br>0491 836 254</p>
    </div>
  </section>

</body>
</html>
```